Business Card for TVK, logo files already created

Please, can you assist with creating a Business card the TVK graphics which are already listed on www.brinmoretech.example
The business card should be modern and upmarket, textured designs are welcome. Please feel free to express yourself and be very bold with your design.

Target Market(s)

Cyber Security

Industry/Entity Type

Information Technology

Contact Information for Business Card

Company Name
Name
Title
Mobile
Fax or Tel
email
url

Font styles to use
Serif
Sans Serif

Colors
3277b5
85acd3
ffffff

```html
<!DOCTYPE html>
<html lang="en">
<head>
<meta charset="utf-8">
<title>TVK Business Card</title>
<link href="https://fonts.googleapis.com/css2?family=Maven+Pro:wght@400;500;700;800&display=swap" rel="stylesheet">
<style>
  :root {
    --backdrop: #3a3a3c;
    --navy: #27378a;
    --navy-deep: #1d2a6e;
    --navy-light: #34499e;
    --mark-ink: #16205a;
    --swoosh: #4a4a4e;
    --ink: #3c3c40;
    --white: #ffffff;
  }
  * { margin: 0; padding: 0; box-sizing: border-box; }
  html, body { width: 1200px; height: 900px; overflow: hidden; }
  body {
    background: var(--backdrop);
    font-family: "Maven Pro", sans-serif;
    position: relative;
  }
  .card {
    position: absolute;
    left: 280px;
    width: 640px;
    height: 366px;
    overflow: hidden;
    box-shadow: 0 10px 30px rgba(0,0,0,.45);
  }
  .card-back {
    top: 40px;
    background: linear-gradient(120deg, var(--navy-deep), var(--navy) 55%, var(--navy-light));
  }
  .back-name {
    position: absolute;
    top: 120px; left: 0; right: 0;
    text-align: center;
    font-size: 104px;
    font-weight: 800;
    letter-spacing: -2px;
    color: var(--mark-ink);
    line-height: 1;
  }
  .back-url {
    position: absolute;
    bottom: 34px; left: 0; right: 0;
    text-align: center;
    color: var(--white);
    font-size: 17px;
    letter-spacing: .5px;
  }
  .card-front {
    top: 484px;
    height: 366px;
    background: var(--white);
  }
  .front-wave { position: absolute; inset: 0; }
  .front-name {
    position: absolute;
    top: 26px; left: 30px;
    font-size: 58px;
    font-weight: 800;
    letter-spacing: -1px;
    color: var(--navy);
    line-height: 1;
  }
  .contact-list {
    position: absolute;
    top: 150px; left: 60px;
    list-style: none;
  }
  .contact-list li {
    display: flex;
    align-items: center;
    gap: 10px;
    height: 26px;
    font-size: 18px;
    color: var(--ink);
    letter-spacing: .5px;
  }
  .contact-list svg { width: 17px; height: 17px; fill: var(--navy); flex: none; }
  .holder {
    position: absolute;
    top: 170px; right: 48px;
    text-align: right;
  }
  .holder-name { font-size: 28px; font-weight: 500; color: var(--navy); line-height: 1.1; }
  .holder-title { font-size: 17px; color: var(--ink); }
  .edge-tab {
    position: absolute;
    top: 182px; right: 0;
    width: 9px; height: 40px;
    background: var(--navy);
  }
  .front-url {
    position: absolute;
    right: 48px; bottom: 22px;
    color: var(--white);
    font-size: 18px;
    letter-spacing: .5px;
  }
</style>
</head>
<body>
  <section class="card card-back">
    <div class="back-name">TVK</div>
    <div class="back-url">www.brinmoretech.example</div>
  </section>

  <section class="card card-front">
    <svg class="front-wave" viewBox="0 0 640 366" preserveAspectRatio="none">
      <path fill="var(--navy)" d="M0,232 C90,300 200,305 300,302 C420,298 540,262 640,300 L640,366 L0,366 Z"/>
      <path fill="var(--swoosh)" d="M0,210 C50,250 130,272 240,280 C130,282 50,262 0,236 Z"/>
    </svg>

    <div class="front-name">TVK</div>

    <ul class="contact-list">
      <li>
        <svg viewBox="0 0 24 24"><path d="M6.6 10.8a15.1 15.1 0 0 0 6.6 6.6l2.2-2.2c.3-.3.7-.4 1-.2 1.1.4 2.3.6 3.6.6.6 0 1 .4 1 1V20c0 .6-.4 1-1 1A17 17 0 0 1 3 4c0-.6.4-1 1-1h3.5c.6 0 1 .4 1 1 0 1.3.2 2.5.6 3.6.1.3 0 .7-.2 1z"/></svg>
        800 - 555 - 0146
      </li>
      <li>
        <svg viewBox="0 0 24 24"><path d="M6 2h10v5H6zM3 8h18v12H3zm3 3v2h3v-2zm5 0v2h3v-2zm-5 4v2h3v-2zm5 0v2h3v-2zm5-4v6h3v-6z"/></svg>
        800 - 555 - 0155
      </li>
      <li>
        <svg viewBox="0 0 24 24"><path d="M2 5h20v14H2zm2 2v.5l8 5 8-5V7z"/></svg>
        contact@brinmoretech.example
      </li>
    </ul>

    <div class="holder">
      <div class="holder-name">Daniel Reyes</div>
      <div class="holder-title">Founder</div>
    </div>
    <div class="edge-tab"></div>

    <div class="front-url">www.brinmoretech.example</div>
  </section>
</body>
</html>
```